A land page lead collector for people who want to reduce there postage costs

We are looking to create a single page website landing page to collect leads of people who want to reduce there postage costs.

The form should basically ask:

Name:
Business Name:
Address:
Town:
Post Code:
Email:
Phone:
Letter Volume Per Week:
Parcel Volume Per Week:

We should basically be advertising cheaper postage costs.

We will not be showing prices on this website we will just be collecting the leads.

Our competition website is as follows https://parcelwrenhub.com

But we are not a online service. This is just a collector to get leads of people who want to save money on there postage costs.
Updates

Target Market(s)

Small and medium sized enterprises

Industry/Entity Type

Advertising

Number of Pages Required

1 page

Colors
ec2027
0356a4

Requirements
Must have
• Form above the fold of the page
Nice to have
• Colour red and blue.
• Parallax design would be nice.

```html
<!DOCTYPE html>
<html lang="en">
<head>
<meta charset="utf-8">
<title>Thrift Post – Reduce Your Postage Costs</title>
<link href="https://fonts.googleapis.com/css2?family=Lato:ital,wght@0,400;0,700;1,400&display=swap" rel="stylesheet">
<style>
:root{
  --red:#ec2027;
  --blue:#0356a4;
  --ink:#333333;
  --muted:#666666;
  --panel:#efefef;
  --field-border:#555555;
  --placeholder:#8a8a8a;
  --quote-bg:#e4e4e4;
  --white:#ffffff;
}
*{box-sizing:border-box;margin:0;padding:0}
html,body{width:799px;height:1200px;overflow:hidden}
body{position:relative;font-family:'Lato',sans-serif;color:var(--ink);background:var(--white)}
.abs{position:absolute}

/* hero */
.hero{left:0;top:0;width:799px;height:418px;background:linear-gradient(120deg,#3a2424 0%,#5a1f20 45%,#8a7a78 75%,#d8d4d0 100%)}
.brand-tag{left:116px;top:0;width:232px;height:78px;background:var(--white);border:3px solid var(--red);border-top:none;display:flex;align-items:center;justify-content:center}
.brand-tag span{font-size:30px;font-weight:700;color:var(--blue);letter-spacing:1px}
.hero-caption{left:115px;top:187px;width:270px;height:193px;background:rgba(70,70,70,.55);padding:6px 7px}
.hero-caption p{color:var(--white);font-size:18px;font-weight:700;line-height:29.4px}
.dots{left:122px;top:360px;display:flex;gap:4px}
.dots i{width:8px;height:8px;border-radius:50%;background:#bbb;display:block}
.dots i:first-child{background:var(--red)}

/* section titles */
.section-title{left:0;width:799px;text-align:center;font-weight:700;color:var(--ink)}

/* about */
.about-title{top:448px;font-size:23px}
.about-title .name{color:var(--blue)}
.about-text{left:100px;width:599px;text-align:center;font-size:7.5px;line-height:13px;color:var(--muted)}

/* form */
.callout{left:0;top:582px;width:799px;height:278px;background:var(--panel)}
.callout-title{top:604px;font-size:24px}
.field{height:25px;border:1px solid var(--field-border);background:var(--panel);box-shadow:inset 1px 1px 0 #fff;font-style:italic;font-size:10px;color:var(--placeholder);padding:6px 7px}
.submit{left:342px;top:801px;width:116px;height:30px;background:var(--blue);color:var(--white);font-weight:700;font-size:14px;display:flex;align-items:center;justify-content:center}

/* benefits */
.benefits-title{top:883px;font-size:23px}
.benefit{top:920px;width:275px}
.benefit h3{font-size:11.5px;font-weight:400;color:var(--ink);display:flex;align-items:center;gap:6px;margin-bottom:4px}
.benefit p{font-size:7.5px;line-height:12.5px;color:var(--muted);padding-left:17px;letter-spacing:.2px}
.arrow{width:23px;height:23px}

/* reviews */
.reviews{left:0;top:990px;width:799px;height:178px;background:var(--panel)}
.reviews-title{top:1015px;font-size:21px}
.avatar{width:56px;height:56px;border-radius:50%;background:radial-gradient(circle at 50% 40%,#c9b3a4,#7d6a60);border:3px solid #fff;box-shadow:0 6px 6px -4px rgba(0,0,0,.3)}
.quote{width:190px;height:64px;background:var(--quote-bg);padding:5px 7px 0 7px;font-style:italic;font-size:8.8px;line-height:13.6px;text-align:center;color:var(--ink)}
.quote b{font-style:normal;font-size:18px;color:#aaa;float:left;line-height:14px;margin-right:2px}
.reviewer{font-size:9px;color:var(--ink)}

/* footer */
.footer{left:0;top:1168px;width:799px;height:32px;background:var(--blue);color:#dfe8f4;font-size:8px;display:flex;align-items:center;justify-content:center}
</style>
</head>
<body>

<div class="abs hero" role="img" aria-label="Photo of a smiling woman handing over a stamped envelope at a post office counter"></div>
<div class="abs brand-tag"><span>THRIFT POST</span></div>
<div class="abs hero-caption"><p>Lorem ipsum dolor sit amet, consectetuer adipiscing elit, sed Lorem ipsum dolor sit amet, consectetuer adipiscing elit, sed</p></div>
<div class="abs dots"><i></i><i></i><i></i><i></i></div>

<h2 class="abs section-title about-title">ABOUT <span class="name">THRIFT POST</span></h2>
<p class="abs about-text" style="top:491px">Lorem ipsum dolor sit amet, consectetuer adipiscing elit, sed diam nonummy nibh euismod tincidunt ut laoreet dolore magna<br>aliquam erat volutpat. Ut wisi enim ad minim veniam, quis nostrud exerci tation ullamcorper suscipit lobortis nisl ut aliquip ex eaLorem ipsum dolor sit amet,</p>
<p class="abs about-text" style="top:529px">Lorem ipsum dolor sit amet, consectetuer adipiscing elit, sed diam nonummy nibh euismod tincidunt ut laoreet dolore magna<br>aliquam erat volutpat. Ut wisi enim ad minim veniam, quis nostrud exerci tation ullamcorper suscipit lobortis nisl ut aliquip ex eaLorem ipsum dolor sit amet</p>

<div class="abs callout"></div>
<h2 class="abs section-title callout-title">THE CALLOUT FORM</h2>
<div class="abs field" style="left:115px;top:646px;width:318px">Your Name</div>
<div class="abs field" style="left:444px;top:646px;width:241px">Business Name</div>
<div class="abs field" style="left:115px;top:683px;width:377px">Your Address</div>
<div class="abs field" style="left:503px;top:683px;width:182px">Town</div>
<div class="abs field" style="left:115px;top:721px;width:182px">Post Code</div>
<div class="abs field" style="left:309px;top:721px;width:182px">Email</div>
<div class="abs field" style="left:503px;top:721px;width:182px">Phone</div>
<div class="abs field" style="left:115px;top:758px;width:279px">Letter Volume Per Week</div>
<div class="abs field" style="left:406px;top:758px;width:279px">Parcel Volume Per Week</div>
<div class="abs submit">SUBMIT</div>

<h2 class="abs section-title benefits-title">BENEFITS</h2>
<svg class="abs arrow" style="left:80px;top:930px" viewBox="0 0 23 23"><circle cx="11.5" cy="11.5" r="10.5" fill="none" stroke="#555"/><path d="M13 7l-4 4.5 4 4.5" fill="none" stroke="#555"/></svg>
<svg class="abs arrow" style="left:697px;top:930px" viewBox="0 0 23 23"><circle cx="11.5" cy="11.5" r="10.5" fill="none" stroke="#555"/><path d="M10 7l4 4.5-4 4.5" fill="none" stroke="#555"/></svg>
<div class="abs benefit" style="left:114px">
  <h3><svg width="11" height="11" viewBox="0 0 11 11"><g fill="#555"><rect x="3.5" y="0" width="4" height="4" transform="rotate(45 5.5 2)"/><rect x="3.5" y="7" width="4" height="4" transform="rotate(45 5.5 9)"/><rect x="0" y="3.5" width="4" height="4" transform="rotate(45 2 5.5)"/><rect x="7" y="3.5" width="4" height="4" transform="rotate(45 9 5.5)"/></g></svg>Lorem ipsum dolor sit amet</h3>
  <p>Lorem ipsum dolor sit amet, consectetuer adipiscing elit, sed diam nonummy nibh euismod tincidunt ut laoreet dolore magna</p>
</div>
<div class="abs benefit" style="left:405px">
  <h3><svg width="11" height="11" viewBox="0 0 11 11"><g fill="#555"><rect x="3.5" y="0" width="4" height="4" transform="rotate(45 5.5 2)"/><rect x="3.5" y="7" width="4" height="4" transform="rotate(45 5.5 9)"/><rect x="0" y="3.5" width="4" height="4" transform="rotate(45 2 5.5)"/><rect x="7" y="3.5" width="4" height="4" transform="rotate(45 9 5.5)"/></g></svg>Lorem ipsum dolor sit amet</h3>
  <p>Lorem ipsum dolor sit amet, consectetuer adipiscing elit, sed diam nonummy nibh euismod tincidunt ut laoreet dolore magna</p>
</div>

<div class="abs reviews"></div>
<h2 class="abs section-title reviews-title">CUSTOMER REVIEWS</h2>
<svg class="abs arrow" style="left:80px;top:1084px" viewBox="0 0 23 23"><circle cx="11.5" cy="11.5" r="10.5" fill="none" stroke="#555"/><path d="M13 7l-4 4.5 4 4.5" fill="none" stroke="#555"/></svg>
<svg class="abs arrow" style="left:697px;top:1084px" viewBox="0 0 23 23"><circle cx="11.5" cy="11.5" r="10.5" fill="none" stroke="#555"/><path d="M10 7l4 4.5-4 4.5" fill="none" stroke="#555"/></svg>
<div class="abs avatar" style="left:117px;top:1057px" role="img" aria-label="Portrait photo of customer Alan Mercer"></div>
<div class="abs quote" style="left:192px;top:1054px"><b>&ldquo;</b>Lorem ipsum dolor sit amet, consectetuer adipiscing elit, sed diam nonummy nibh euismod tincidunt ut laoreet dolore magna aliquam erat volutpat.</div>
<div class="abs reviewer" style="left:218px;top:1130px">Mr. Alan Mercer</div>
<div class="abs avatar" style="left:419px;top:1057px" role="img" aria-label="Portrait photo of customer Clara Whitby"></div>
<div class="abs quote" style="left:494px;top:1054px"><b>&ldquo;</b>Lorem ipsum dolor sit amet, consectetuer adipiscing elit, sed diam nonummy nibh euismod tincidunt ut laoreet dolore magna aliquam erat volutpat.</div>
<div class="abs reviewer" style="left:520px;top:1130px">Miss Clara Whitby</div>

<footer class="abs footer">&copy; 2015 Thriftpost. &nbsp;&nbsp;| &nbsp;&nbsp;All Rights Reserved.</footer>

</body>
</html>
```